Create an Empowering Website for Corinne Albadeau on Wix with Mailing List Integration

I'm looking for a talented Wix designer and developer to craft an inspiring website for my personal brand, Corinne Albadeau. As a Motivational Speaker, Author, Success and Executive Coach, I'm dedicated to empowering women to pursue their dreams and believe in themselves.

The website will serve as a hub for empowerment, offering valuable resources, services, and products. Here's what I need:

Booking System: Enable visitors to easily book coaching sessions and speaking engagements. The booking process should be smooth and user-friendly.

Online Courses: Showcase my empowering online courses and workshops, allowing visitors to enroll directly on the website. The design should highlight the value and impact of each course.

Product Store: Create an online store to sell my bestselling book, merchandise, and other products. The store should have an intuitive interface for browsing and purchasing.

Event Ticketing: Allow visitors to purchase tickets for upcoming events, workshops, and seminars. The ticketing system should integrate seamlessly with Wix and offer secure payment options.

About Me Section: Provide a compelling overview of my background, expertise, and mission. Include testimonials and achievements to build credibility and trust.

Blog & Resources: Maintain a blog section to share empowering insights, tips, and resources. Encourage visitors to subscribe for updates and share content on social media.

Contact & Connect: Make it easy for visitors to get in touch and connect with me on social media platforms. Include a contact form and clear calls-to-action throughout the website.

Mailing List Signup: Incorporate a mailing list signup form to capture visitors' email addresses. Offer incentives such as exclusive content or discounts to encourage signups.

The website should exude a modern, sleek, and empowering vibe that resonates with my brand. Utilize empowering imagery, vibrant colors, and engaging visuals to captivate visitors and inspire them to take action.

If you have experience in designing and developing empowering websites on the Wix platform with mailing list integration, I'd love to see your portfolio and discuss how we can bring my vision to life. Let's create a captivating online platform that empowers women to thrive with Corinne Albadeau.

Target Market(s)

Woman

Coding

Coded - Design and coding required

Requirements
Must have
• Clean and Modern

```html
<!DOCTYPE html>
<html lang="en">
<head>
<meta charset="utf-8">
<title>Corinne Albadeau — Website Pages</title>
<link href="https://fonts.googleapis.com/css2?family=Cinzel:wght@400;600;700&family=Montserrat:wght@400;500;600;700&display=swap" rel="stylesheet">
<style>
:root{
  --ink:#1d1b22;
  --dark:#17151c;
  --night:#0f0e13;
  --plum:#8d1d7d;
  --plum-deep:#4a1845;
  --cyan:#39bcd8;
  --lav:#eeeefa;
  --mist:#e9f5fa;
  --blush:#f7f0f7;
  --grey:#f3f3f4;
  --grey2:#e6e6e8;
  --text:#4b4a50;
  --forest:#1f3a26;
  --line:#d7d5dc;
}
*{box-sizing:border-box;margin:0;padding:0}
html,body{width:1070px;height:1200px;overflow:hidden;background:#fff}
body{font-family:"Montserrat",sans-serif;color:var(--text)}
.stage{position:absolute;left:0;top:0;width:1810px;height:2030px;transform:scale(.5912);transform-origin:0 0}
.page{position:absolute;top:42px;width:310px;background:#fff;box-shadow:0 1px 6px rgba(0,0,0,.25);overflow:hidden}
.serif{font-family:"Cinzel",serif}
section{position:relative;overflow:hidden}
.abs{position:absolute}
.ph{position:absolute;border-radius:1px}
/* header */
.topbar{height:13px;background:#101014;color:#ddd;font-size:2.6px;display:flex;justify-content:space-between;align-items:center;padding:0 26px}
.topbar b{text-decoration:underline;color:#fff}
.nav{position:absolute;left:0;right:0;top:6px;height:20px;display:flex;align-items:center;padding:0 24px;z-index:3}
.logo{display:flex;flex-direction:column;align-items:center;gap:1px}
.logo i{width:9px;height:9px;border:.6px solid currentColor;border-radius:50%;display:block}
.logo span{font-family:"Cinzel",serif;font-size:3.4px;letter-spacing:.2px;white-space:nowrap}
.nav .logo{color:#fff}
.nav ul{list-style:none;display:flex;gap:6px;margin-left:auto;font-family:"Cinzel",serif;font-size:3.3px;color:#fff;align-items:center}
.nav li.on{color:#d45ac4}
.btn{display:inline-block;background:var(--plum);color:#fff;font-family:"Cinzel",serif;font-size:3.3px;padding:2.5px 5px;letter-spacing:.2px}
.btn.cyan{background:var(--cyan)}
.nav .btn{padding:2.5px 3.5px;outline:.5px solid rgba(255,255,255,.6)}
/* heroes */
.hero{position:relative;background:linear-gradient(120deg,#2a2629,#151317 60%,#241c22)}
.hero h1{font-family:"Cinzel",serif;color:#fff;font-weight:400;font-size:9.5px;line-height:12px;letter-spacing:.3px}
.hero p{color:#e6e3e8;font-size:2.9px;line-height:4.6px}
.h2{font-family:"Cinzel",serif;color:var(--ink);font-size:7.5px;letter-spacing:.3px;text-align:center;font-weight:400}
.h2 em{font-style:normal;color:var(--plum)}
.light .h2{color:#fff}
.small{font-size:2.8px;line-height:4.4px}
.center{text-align:center}
/* cards */
.card{position:absolute;background:#fff;box-shadow:0 0 3px rgba(0,0,0,.18);border-radius:2px;padding:3px;text-align:center}
.card .ph{position:relative;display:block;height:52px;width:100%}
.card h4{font-family:"Cinzel",serif;font-size:3.4px;color:var(--ink);font-weight:600;margin:4px 0 2px}
.card h5{font-size:3.2px;color:var(--ink);font-weight:700;margin:4px 0 2px}
.card p{font-size:2.5px;line-height:3.7px}
.pill{display:inline-block;background:#3a2f7e;color:#fff;font-size:2.4px;font-weight:700;border-radius:4px;padding:1.6px 5px;margin-top:3px}
/* footer */
.foot{background:var(--grey);height:70px;display:flex;align-items:center;padding:0 28px;gap:14px;color:var(--text)}
.foot .logo{color:#555}
.foot .sep{width:.6px;height:28px;background:var(--plum)}
.foot .con{font-family:"Cinzel",serif;font-size:3px;color:#333}
.soc{display:flex;gap:3px;margin-top:4px;justify-content:center}
.soc i{width:3.4px;height:3.4px;border-radius:50%;background:#2d2d33;display:block}
.foot .cols{display:flex;gap:24px;font-size:2.6px;line-height:4.2px;color:#333}
.bottom{background:var(--grey2);height:36px;font-size:2.6px;text-align:center;color:#333;padding-top:10px;line-height:4.3px;position:relative}
.bottom span{position:absolute;right:14px;top:13px;font-size:2.2px}
.field{background:#fff;height:7px;border:.4px solid #ccc;font-size:2.2px;color:#999;padding:1.8px 2px}
label{font-size:2.3px;color:#eee;display:block;margin-bottom:1px}
ul.bul{list-style:none;font-size:2.7px;line-height:4.2px}
ul.bul li::before{content:"";display:inline-block;width:2px;height:2px;border-radius:50%;background:currentColor;margin-right:3px;vertical-align:middle}
</style>
</head>
<body>
<div class="stage">

<!-- PAGE 1 : HOME -->
<div class="page" style="left:52px;height:1958px">
  <div class="topbar"><span>555-014-2270</span><span>Check Out Corinne's Latest Book: <b>SWEETHEART, RISE UP</b></span><span>hello@corinnealbadeau.com</span></div>
  <section class="hero" style="height:190px">
    <div class="ph" role="img" aria-label="Group of smiling women standing in front of a brick wall" style="inset:0;background:linear-gradient(180deg,rgba(60,45,45,.55),rgba(20,18,22,.85)),linear-gradient(90deg,#4a3a36,#2b2426 50%,#3d3131)"></div>
    <div class="nav"><div class="logo"><i></i><span>Corinne Albadeau</span></div>
      <ul><li>About</li><li>Speaker</li><li>Coach</li><li>Courses</li><li>Events</li><li>Shop</li><li class="btn">Contact Us</li></ul></div>
    <div class="abs center" style="left:20px;right:20px;top:73px">
      <h1>EMPOWERING WOMEN<br>TO PURSUE THEIR WILDEST DREAMS</h1>
      <p style="margin:5px 40px 0">Welcome to the official website of Corinne Albadeau. As a Motivational Speaker, Author, Success and Executive Coach, she is dedicated to helping women unlock their full potential, achieve their dreams, and believe in themselves.</p>
      <div style="margin-top:7px;display:flex;gap:4px;justify-content:center"><span class="btn">Book a Session</span><span class="btn cyan">Inquire About Speaking</span></div>
      <div style="margin-top:7px;display:flex;gap:4px;justify-content:center;align-items:center;color:#fff;font-size:2.8px;font-weight:700">
        <svg width="12" height="12" viewBox="0 0 12 12"><circle cx="6" cy="6" r="6" fill="#fff"/><path d="M4.6 3.6 8.4 6 4.6 8.4z" fill="#222"/></svg>WATCH CORINNE IN ACTION</div>
    </div>
  </section>
  <section style="height:90px" class="center">
    <p class="serif" style="font-size:7px;line-height:10px;color:var(--ink);padding-top:22px">YOU ARE POTENT; NEVER LET ANYONE DILUTE<br><span style="color:var(--plum)">WHAT GOD HAS PLACED IN YOU.</span><br>YOU ARE WHAT THE WORLD HAS BEEN<br>WAITING ON.</p>
  </section>
  <section style="height:198px;background:linear-gradient(90deg,#1b1a1f,#2a282d)" class="light">
    <div class="ph" role="img" aria-label="Portrait of Corinne in a black and white patterned blazer" style="right:0;top:20px;width:120px;height:178px;background:linear-gradient(180deg,#3a3638,#1a181b)"></div>
    <div class="abs" style="left:26px;top:26px;width:150px;color:#e2e0e4">
      <p class="serif" style="font-size:6.5px;color:#fff">MEET CORINNE <span style="color:#d45ac4">ALBADEAU</span></p>
      <p class="small" style="margin-top:6px">Corinne Albadeau is a dynamic force in the world of empowerment and personal growth. With a passion for helping women achieve their dreams and unlock their full potential, Corinne offers a unique blend of inspiration, expertise, and guidance.</p>
      <ul class="bul" style="margin-top:4px;font-size:2.6px;line-height:3.9px">
        <li><b style="color:var(--cyan)">Motivational Speaker:</b> Inspiring audiences worldwide with her powerful message.</li>
        <li><b style="color:var(--cyan)">Author:</b> Sharing her journey and insights in her book.</li>
        <li><b style="color:var(--cyan)">Success Coach:</b> Offering personalized coaching to help women overcome obstacles and thrive.</li>
        <li><b style="color:var(--cyan)">Executive Coach:</b> Guiding female leaders to new heights of success with strategies and support.</li>
      </ul>
      <span class="btn" style="background:transparent;border:.5px solid #fff;margin-top:8px">Read Corinne Albadeau Full Bio</span>
    </div>
  </section>
  <section style="height:167px" class="center">
    <p style="font-size:3.2px;color:#333;padding-top:20px">Experience how Corinne helps you</p>
    <p class="h2" style="margin-top:5px">CORINNE ALBADEAU</p>
    <div class="ph" role="img" aria-label="Video still of Corinne speaking" style="left:73px;top:55px;width:170px;height:99px;background:linear-gradient(135deg,#5a3a48,#3a2530)"></div>
    <svg class="abs" style="left:151px;top:97px" width="14" height="14" viewBox="0 0 14 14"><circle cx="7" cy="7" r="6" fill="none" stroke="#fff" stroke-width=".8"/><path d="M5.6 4.5 9.6 7l-4 2.5z" fill="#fff"/></svg>
  </section>
  <section style="height:193px">
    <p class="h2" style="font-size:6.5px;line-height:9px;padding-top:10px">EMBARK ON A JOURNEY OF SELF-<br>DISCOVERY <em>AND EMPOWERMENT WITH</em></p>
    <p class="center" style="font-size:4px;font-weight:700;color:var(--ink);margin-top:4px">"SWEETHEART, RISE UP!"</p>
    <div class="ph" role="img" aria-label="Promotional artwork of the book with author photos" style="left:34px;top:55px;width:108px;height:110px;background:linear-gradient(160deg,#f6e3f1,#d85cb5 50%,#5ac3e0);box-shadow:0 0 3px rgba(0,0,0,.25)"></div>
    <div class="abs" style="left:160px;top:55px;width:125px;color:#333">
      <p style="font-size:2.5px;line-height:3.8px">In the midst of life's hustle, where countless thoughts bombard us, "Sweetheart, Rise Up!" stands as a guiding light to affirm your inherent worth and untapped potential.</p>
      <ul class="bul" style="font-size:2.5px;line-height:3.9px;margin-top:2px">
        <li><b>Self-Discovery:</b> Explore and embrace your unique identity.</li>
        <li><b>Empowerment:</b> Walk in the power within you.</li>
        <li><b>Reflection:</b> Take time to reflect on your journey and affirm your uniqueness.</li>
        <li><b>Solutions:</b> Discover the solutions that lie within you.</li>
      </ul>
      <p style="font-size:2.5px;line-height:3.8px">Start your journey today with <b>"SWEETHEART, RISE UP!"</b> and uncover the power within you!</p>
      <span class="btn" style="margin-top:6px">Buy Now</span>
    </div>
  </section>
  <div style="height:.6px;background:#b677ad;margin:0 62px"></div>
  <section style="height:195px">
    <p class="h2" style="padding-top:16px">CLIENT <em>LOVE</em></p>
    <div class="card" style="left:35px;top:40px;width:113px;height:116px">
      <div class="ph" role="img" aria-label="Client portrait" style="position:relative;margin:0 auto;width:24px;height:24px;border-radius:50%;background:linear-gradient(#caa28b,#7a5646)"></div>
      <h4>DELPHINE</h4><p>My coaching experience with Corinne Albadeau has given me new insight on ways to better achieve my long term goals through everyday practices. The sessions helped me set better goals and find better ways to obtain them by taking more effective and focused actions.</p>
      <span class="btn" style="margin-top:6px;padding:2px 5px">Read More</span></div>
    <div class="card" style="left:165px;top:40px;width:113px;height:116px">
      <div class="ph" role="img" aria-label="Client portrait" style="position:relative;margin:0 auto;width:24px;height:24px;border-radius:50%;background:linear-gradient(#e0b98a,#6a5040)"></div>
      <h4>MARISOL</h4><p>The coaching sessions with Corinne were pretty awesome. Corinne really gives you the correct action steps that help you move forward and plan the next steps for your goals and career. She succeeds in getting to know you and helping you define your needs and skills.</p>
      <span class="btn" style="margin-top:6px;padding:2px 5px">Read More</span></div>
  </section>
  <section style="height:155px;background:linear-gradient(90deg,#2a1329,#5a1f52 60%,#3b1638)">
    <div class="ph" role="img" aria-label="Corinne smiling with arms crossed in a purple dress" style="left:22px;top:-8px;width:112px;height:163px;background:linear-gradient(180deg,#5c3650,#3a1a34)"></div>
    <div class="abs" style="left:138px;top:26px;width:150px">
      <p class="serif" style="font-size:6.5px;line-height:9px;color:#fff">BOOK CORINNE FOR YOUR<br>UPCOMING EVENT</p>
      <div style="display:grid;grid-template-columns:1fr 1fr;gap:4px 10px;margin-top:8px">
        <div><label>Name *</label><div class="field" style="height:6px"></div></div>
        <div><label>&nbsp;</label><div class="field" style="height:6px"></div></div>
        <div><label>Email *</label><div class="field" style="height:6px"></div></div>
        <div><label>Phone Number *</label><div class="field" style="height:6px"></div></div>
      </div>
      <span class="btn" style="margin-top:9px;padding:2px 6px">Submit</span>
    </div>
  </section>
  <section style="height:220px;background:var(--lav)">
    <p class="h2" style="padding-top:20px">ONLINE COURSES</p>
    <p class="center small" style="font-size:2.7px;margin:4px 80px 0">Discover courses built to grow your confidence, sharpen your purpose and help you lead boldly.</p>
    <div class="card" style="left:26px;top:66px;width:80px;height:117px"><div class="ph" role="img" aria-label="Woman in a yoga pose" style="height:52px;background:linear-gradient(#c9d6de,#8aa0ad)"></div><h5>GROW YOUR VOICE</h5><p>Build calm, clear confidence for every room you step into.</p><span class="pill">BOOK NOW</span></div>
    <div class="card" style="left:115px;top:76px;width:80px;height:117px"><div class="ph" role="img" aria-label="Woman working on a laptop" style="height:52px;background:linear-gradient(#d6dde4,#8e9aa6)"></div><h5>LEAD WITH HEART</h5><p>Practical tools to lead teams with clarity and care.</p><span class="pill">BOOK NOW</span></div>
    <div class="card" style="left:204px;top:66px;width:80px;height:117px"><div class="ph" role="img" aria-label="Woman at a desk by a window" style="height:52px;background:linear-gradient(#e2e2e2,#9a9a9a)"></div><h5>PLAN YOUR YEAR</h5><p>Set goals that fit your life and keep them all year long.</p><span class="pill">BOOK NOW</span></div>
    <svg class="abs" style="left:8px;top:120px" width="8" height="8" viewBox="0 0 8 8"><circle cx="4" cy="4" r="4" fill="#ccc"/><path d="M4.6 2.4 3 4l1.6 1.6" stroke="#fff" stroke-width=".8" fill="none"/></svg>
    <svg class="abs" style="left:292px;top:120px" width="8" height="8" viewBox="0 0 8 8"><circle cx="4" cy="4" r="4" fill="#3a2f7e"/><path d="M3.4 2.4 5 4 3.4 5.6" stroke="#fff" stroke-width=".8" fill="none"/></svg>
  </section>
  <section style="height:197px">
    <p class="h2" style="padding-top:22px">JOIN THE <em>COMMUNITY</em></p>
    <p class="center small" style="font-size:2.7px;margin:5px 60px 0">Become part of Corinne Albadeau's empowering network. Stay updated, get inspired, and connect with like-minded women.</p>
    <div class="card" style="left:35px;top:63px;width:113px;height:108px"><div class="ph" role="img" aria-label="Women laughing together" style="height:62px;background:linear-gradient(#d8b9a0,#8b6a58)"></div><h4>RISING LIFE GROUP</h4><p style="color:var(--cyan);text-decoration:underline">Join our transformative<br>Bible Study group.</p></div>
    <div class="card" style="left:165px;top:63px;width:113px;height:108px"><div class="ph" role="img" aria-label="Woman smiling at a laptop" style="height:62px;background:linear-gradient(#c9a58b,#6f4e44)"></div><h4>TRUST HER CIRCLE GROUP</h4><p style="color:var(--cyan);text-decoration:underline">Engage with our community<br>and share your journey.</p></div>
  </section>
  <section style="height:85px;background:#eef0fb">
    <p class="h2" style="padding-top:18px">MAILING LIST</p>
    <p class="center" style="font-size:2.8px;margin-top:4px">Receive the latest updates, inspiration, and special offers.</p>
    <div class="abs" style="left:30px;right:30px;top:48px;display:flex;gap:4px">
      <div class="field" style="flex:1">Name</div><div class="field" style="flex:1">Email</div><span class="btn" style="width:52px;text-align:center">Submit</span></div>
  </section>
  <section style="height:150px">
    <p class="h2" style="padding-top:22px">UPCOMING EVENTS</p>
    <div class="card" style="left:26px;top:46px;width:125px;height:78px;text-align:left;display:flex;gap:4px">
      <div class="ph" role="img" aria-label="Event poster with Corinne" style="position:relative;width:60px;height:72px;flex:none;background:linear-gradient(#c79a3a,#2e2420)"></div>
      <div><span style="font-size:2.2px;background:#e3e6f7;padding:1px 2px;color:#3a2f7e">24 MAY 2024</span><p style="font-size:2.4px;font-weight:700;color:var(--ink);margin-top:3px">RISE AND SHINE BRUNCH, SPRING EDITION</p><p style="margin-top:2px">An afternoon of talks, music and honest stories with women on the rise.</p><p style="color:var(--plum);font-weight:700;margin-top:2px">READ MORE</p></div></div>
    <div class="card" style="left:160px;top:46px;width:125px;height:78px;text-align:left;display:flex;gap:4px">
      <div class="ph" role="img" aria-label="Event poster in purple tones" style="position:relative;width:60px;height:72px;flex:none;background:linear-gradient(#b04f9a,#2b1a2c)"></div>
      <div><span style="font-size:2.2px;background:#e3e6f7;padding:1px 2px;color:#3a2f7e">24 MAY 2024</span><p style="font-size:2.4px;font-weight:700;color:var(--ink);margin-top:3px">PURPOSE NIGHT LIVE, ONE EVENING ONLY</p><p style="margin-top:2px">A night of worship, reflection and practical steps toward your calling.</p><p style="color:var(--plum);font-weight:700;margin-top:2px">READ MORE</p></div></div>
  </section>
  <div class="foot"><div class="logo"><i></i><span>Corinne Albadeau</span></div><div class="sep"></div><div><div class="con">Connect With Corinne</div><div class="soc"><i></i><i></i><i></i><i></i></div></div><div class="cols"><div>Home<br>Videos<br>Virtual<br>Meeting Professionals</div><div>Workshops<br>About Corinne<br>Speaking</div></div></div>
  <div class="bottom">©Corinne Albadeau. All Rights Reserved.<br>Sitemap | Privacy Policy<span>EN</span></div>
</div>

<!-- PAGE 2 : ABOUT -->
<div class="page" style="left:403px;height:1263px">
  <div class="topbar"><span>555-014-2270</span><span>Check Out Corinne's Latest Book: <b>SWEETHEART, RISE UP</b></span><span>hello@corinnealbadeau.com</span></div>
  <section class="hero" style="height:145px;background:linear-gradient(110deg,#15162a,#1e2340 60%,#141526)">
    <div class="ph" role="img" aria-label="Corinne in a blue blazer, arms crossed" style="right:40px;top:30px;width:100px;height:115px;background:linear-gradient(180deg,#34406a,#1a2040)"></div>
    <div class="nav"><div class="logo"><i></i><span>Corinne Albadeau</span></div><ul><li>Home</li><li class="on">About</li><li>Speaker</li><li>Coach</li><li>Courses</li><li>Events</li><li>Shop</li><li class="btn">Contact Us</li></ul></div>
    <div class="abs" style="left:26px;top:58px;width:125px"><h1 style="font-size:8px;line-height:13px">ABOUT<br>CORINNE V. ALBADEAU</h1>
      <p style="margin-top:3px;font-size:2.6px;line-height:4px">Corinne V. Albadeau, author of Sweetheart, Rise Up, is a dynamic force in the realm of empowerment and personal growth. As a storyteller, motivational speaker, and certified success and executive coach, Corinne is dedicated to helping individuals unlock their full potential and realize their worth.</p></div>
  </section>
  <section style="height:320px">
    <p class="h2" style="font-size:6.5px;padding-top:14px">CORINNE V. ALBADEAU <em>LONG BIO</em></p>
    <div class="abs" style="left:24px;right:24px;top:50px;columns:2;column-gap:14px;font-size:2.3px;line-height:3.6px;color:#555">
      <p>Corinne V. Albadeau embodies the essence of empowerment and leadership. As an influential motivational speaker, coach, and change agent, she touches lives on both individual and organizational levels, fostering holistic success and nurturing future leaders through her various endeavors. Her commitment to guiding individuals to align their purpose with their passion underscores her dedication to seeing her clients thrive.</p><br>
      <p>Born to hard-working immigrant parents, Corinne's unique cultural heritage and life experiences have ingrained in her the importance of resilience and the belief that with courage, anything is possible. Guided by her faith, her work is infused with warmth, enthusiasm, and the spirit of triumph, encouraging individuals to see beyond their challenges and empowering them to transcend barriers and embrace their own stories.</p><br>
      <p>Her role as the Founder and President of a youth leadership nonprofit reflects her deep-rooted commitment to youth development and empowerment, particularly for underserved communities. Through this organization, Corinne provides invaluable coaching and support, equipping young people with the skills and confidence needed to navigate life successfully.</p><br>
      <p>Corinne's impressive involvement in nonprofits and civic councils across her region, her performing arts church, and local women's networks demonstrates her unwavering dedication to community service and advocacy.</p><br>
      <p>As the CEO of Bright Encore Studio, Corinne leverages her passion for philanthropy and a decade's worth of experience in the nonprofit sector to help organizations strengthen their fundraising efforts. She develops personalized messaging, programs, systems, and strategies tailored to each organization's unique needs, optimizing their operations and ensuring their sustainability.</p><br>
      <p>Her educational background in Special Education and a Master's in Business Administration, coupled with certifications in Organizational and Community Leadership and Success and Executive Coaching, illustrates her multifaceted approach to leadership and empowerment.</p><br>
      <p>As a seasoned speaker and facilitator, Corinne has spent years inspiring audiences of all ages to tap into their greatness. Whether through one-on-one coaching sessions or dynamic public speaking engagements, her message is clear: Own your journey, invest in your growth, and greatness will follow.</p><br>
      <p>Corinne is also an author, and her writing, including the empowering phrase "Sweetheart, Rise Up!", resonates as a call to action for personal transformation. Her works inspire and touch the hearts of those seeking joy and authenticity in their lives.</p><br>
      <p>Driven by her love for people and her faith, Corinne's legacy is one of hope, empathy and service. Her work has garnered recognition in various publications, further solidifying her reputation as a beacon of inspiration and positive change in her community and beyond.</p><br>
      <p>As Corinne continues to write and coach, expect a series of works that will guide, inspire, and celebrate the human spirit in all its forms. Corinne V. Albadeau is just getting started.</p>
    </div>
    <span class="btn abs" style="left:136px;top:286px">Book Corinne</span>
  </section>
  <section style="height:212px;background:linear-gradient(180deg,#1a1825,#221f30)">
    <p class="serif center" style="font-size:6.5px;color:#fff;padding-top:22px">ACHIEVEMENTS</p>
    <div class="abs" style="left:24px;top:40px;width:22px;height:22px;border:.8px solid #b64aa8;border-radius:50%"></div>
    <div class="abs" style="left:78px;top:45px;width:200px;color:#ddd"><p class="serif" style="font-size:3.6px;color:#fff">STORYTELLER:</p><p style="font-size:2.5px;line-height:3.8px;margin-top:3px">Corinne captivates audiences with her compelling narratives and authentic storytelling, inspiring others to embrace their own stories and find strength in vulnerability.</p></div>
    <div class="abs" style="left:54px;top:95px;width:22px;height:22px;border:.8px solid #c9a24a;border-radius:50%"></div>
    <div class="abs" style="left:108px;top:98px;width:180px;color:#ddd"><p class="serif" style="font-size:3.6px;color:#fff">MOTIVATIONAL SPEAKER:</p><p style="font-size:2.5px;line-height:3.8px;margin-top:3px">Renowned for her powerful and transformative keynote speeches, Corinne empowers audiences worldwide to believe in themselves, pursue their dreams, and create positive change.</p></div>
    <div class="abs" style="left:24px;top:148px;width:22px;height:22px;border:.8px solid var(--cyan);border-radius:50%"></div>
    <div class="abs" style="left:78px;top:151px;width:210px;color:#ddd"><p class="serif" style="font-size:3.6px;color:#fff">CERTIFIED SUCCESS AND EXECUTIVE COACH:</p><p style="font-size:2.5px;line-height:3.8px;margin-top:3px">With a passion for personal development and growth, Corinne guides clients on a journey of self-discovery, providing the tools and strategies needed to achieve success in both their personal and professional lives.</p></div>
  </section>
  <section style="height:158px;background:#e8e8ea">
    <div class="ph" role="img" aria-label="Corinne in a patterned blouse, thoughtful pose" style="left:24px;top:12px;width:88px;height:146px;background:linear-gradient(180deg,#4b5a46,#1f2620)"></div>
    <p class="abs serif center" style="left:125px;top:32px;width:160px;font-size:3.7px;line-height:7px;color:#333">"YOU ARE WORTH THIS INVESTMENT, BECAUSE YOU ARE YOUR GREATEST ASSET. IT IS TIME TO SHIFT OUR FOCUS AND REALIZE OUR WORTH. WE HAVE ALLOWED OTHERS TO BE OUR VOICE FOR SO LONG, BUT THE TIME HAS NOW COME TO BET ON OURSELVES. INVEST IN YOURSELF AND BECOME THE BEST VERSION OF YOU!"<br><span style="color:var(--plum)">- CORINNE A.</span></p>
  </section>
  <section style="height:235px;border-top:.5px solid #ddd">
    <p class="serif center" style="font-size:3.6px;color:#444;padding-top:14px">DOWNLOADS</p>
    <div class="ph" role="img" aria-label="Corinne in a red jumpsuit with open arms" style="left:178px;top:56px;width:108px;height:150px;border-radius:54px 54px 0 0;background:linear-gradient(180deg,#ecd7c2,#d9b99c)"></div>
    <div class="abs" style="left:24px;top:80px;width:150px">
      <div style="display:flex;justify-content:space-between;align-items:center;height:27px"><span class="serif" style="font-size:4.5px;color:#333">HEADSHOTS</span><span style="font-size:2px">DOWNLOAD HEADSHOTS ⟶</span></div>
      <div style="display:flex;justify-content:space-between;align-items:center;height:27px"><span class="serif" style="font-size:4.5px;color:#333">LONG BIO</span><span style="font-size:2px">DOWNLOAD LONG BIO ⟶</span></div>
      <div style="display:flex;justify-content:space-between;align-items:center;height:27px"><span class="serif" style="font-size:4.5px;color:#333">SHORT BIO</span><span style="font-size:2px">DOWNLOAD SHORT BIO ⟶</span></div>
      <div style="display:flex;justify-content:space-between;align-items:center;height:27px"><span class="serif" style="font-size:4.5px;color:#333">STAGE INTRO</span><span style="font-size:2px">DOWNLOAD STAGE INTRO ⟶</span></div>
      <div style="display:flex;justify-content:space-between;align-items:center;height:27px"><span class="serif" style="font-size:4.5px;color:#333">ONE SHEETER</span><span style="font-size:2px">DOWNLOAD ONE SHEETER ⟶</span></div>
    </div>
  </section>
  <section style="height:70px;background:var(--blush)">
    <p class="serif center" style="font-size:3.6px;line-height:6.2px;color:#333;padding:18px 40px 0">CORINNE'S MISSION IS TO EMPOWER INDIVIDUALS TO EMBRACE THEIR UNIQUE JOURNEY, REALIZE THEIR WORTH, AND BECOME THE BEST VERSION OF THEMSELVES. JOIN HER ON THIS TRANSFORMATIVE JOURNEY TO SELF-DISCOVERY AND PERSONAL GROWTH.</p>
  </section>
  <div class="foot" style="height:80px"><div class="logo"><i></i><span>Corinne Albadeau</span></div><div class="sep"></div><div><div class="con">Connect With Corinne</div><div class="soc"><i></i><i></i><i></i><i></i></div></div><div class="cols"><div>Home<br>Videos<br>Virtual<br>Meeting Professionals</div><div>Workshops<br>About Corinne<br>Speaking</div></div></div>
  <div class="bottom">©Corinne Albadeau. All Rights Reserved.<br>Sitemap | Privacy Policy<span>EN</span></div>
</div>

<!-- PAGE 3 : SPEAKER -->
<div class="page" style="left:753px;height:1136px">
  <div class="topbar"><span>555-014-2270</span><span>Check Out Corinne's Latest Book: <b>SWEETHEART, RISE UP</b></span><span>hello@corinnealbadeau.com</span></div>
  <section class="hero" style="height:145px;background:linear-gradient(110deg,#1e1a1e,#3a2f33 60%,#1a1719)">
    <div class="ph" role="img" aria-label="Corinne in a black and white blazer before an audience" style="right:18px;top:22px;width:110px;height:123px;background:linear-gradient(180deg,#4a4044,#1e1b1d)"></div>
    <div class="nav"><div class="logo"><i></i><span>Corinne Albadeau</span></div><ul><li>Home</li><li>About</li><li class="on">Speaker</li><li>Coach</li><li>Courses</li><li>Events</li><li>Shop</li><li class="btn">Contact Us</li></ul></div>
    <div class="abs" style="left:26px;top:60px;width:150px"><h1 style="font-size:8px;line-height:13px">ENGAGE AND INSPIRE YOUR<br>AUDIENCE</h1>
      <p style="margin-top:4px;font-size:2.6px;line-height:4px">Corinne Albadeau delivers dynamic and motivational keynote speeches that resonate deeply with audiences worldwide. Whether it's a corporate event, conference, or seminar, Corinne's powerful message of empowerment and self-belief leaves a lasting impact.</p></div>
  </section>
  <section style="height:237px;background:var(--lav)">
    <p class="h2" style="padding-top:22px">TOPICS <em>COVERED</em></p>
    <div class="card" style="left:26px;top:43px;width:80px;height:76px"><div class="ph" role="img" aria-label="Group of women smiling" style="height:52px;background:linear-gradient(#e2c8b4,#9a7867)"></div><h4>WOMEN'S EMPOWERMENT</h4></div>
    <div class="card" style="left:115px;top:43px;width:80px;height:76px"><div class="ph" role="img" aria-label="Team collaborating at a table" style="height:52px;background:linear-gradient(#d8c6a8,#7a6c55)"></div><h4>LEADERSHIP DEVELOPMENT</h4></div>
    <div class="card" style="left:204px;top:43px;width:80px;height:76px"><div class="ph" role="img" aria-label="Young people joining hands" style="height:52px;background:linear-gradient(#d9b9a0,#a26a6a)"></div><h4>YOUTH EMPOWERMENT</h4></div>
    <div class="card" style="left:70px;top:127px;width:80px;height:76px"><div class="ph" role="img" aria-label="Speaker presenting to a room" style="height:52px;background:linear-gradient(#d7cfc4,#8d7d72)"></div><h4>MOTIVATIONAL SPEAKING</h4></div>
    <div class="card" style="left:159px;top:127px;width:80px;height:76px"><div class="ph" role="img" aria-label="Woman walking through a city street" style="height:52px;background:linear-gradient(#e9d7c6,#a8846b)"></div><h4>PERSONAL DEVELOPMENT</h4></div>
  </section>
  <section style="height:155px;background:linear-gradient(90deg,#132a1a,#24452d 60%,#17301e)">
    <div class="ph" role="img" aria-label="Corinne in a green dress, arms crossed" style="left:26px;top:-12px;width:110px;height:167px;background:linear-gradient(180deg,#3d6a45,#17301e)"></div>
    <div class="abs" style="left:160px;top:34px;width:130px;color:#ddd">
      <p class="serif" style="font-size:5.5px;color:#fff">WHY BOOK CORINNE?</p>
      <ul class="bul" style="font-size:2.4px;line-height:3.7px;margin-top:8px">
        <li style="margin-bottom:8px">Engaging Storytelling: Captivate your audience with personal stories and practical insights that leave a lasting impression.</li>
        <li style="margin-bottom:8px">Customizable Presentations: Tailor Corinne's message to align perfectly with your event's theme and audience demographics.</li>
        <li>Proven Impact: Experience positive change and inspired action among attendees, driven by Corinne's motivational message.</li></ul></div>
  </section>
  <section style="height:120px" class="center">
    <p class="h2" style="font-size:6px;padding-top:20px">CLIENT TESTIMONIAL</p>
    <div class="ph" role="img" aria-label="Client portrait" style="left:144px;top:38px;width:22px;height:22px;border-radius:50%;background:linear-gradient(#d4b29a,#6f5245)"></div>
    <p style="font-size:2.7px;line-height:4.3px;margin:46px 50px 0">"Corinne's keynote speech was the highlight of our event. Her ability to connect with the audience and deliver a powerful message was truly inspiring."</p>
    <p class="serif" style="font-size:3.2px;color:#333;margin-top:4px">- NOELLE</p>
  </section>
  <section style="height:293px;background:linear-gradient(180deg,#131217,#0c0b10)">
    <p class="serif center" style="font-size:6px;color:#fff;padding-top:24px">SPEAKING OFFERINGS</p>
    <div class="card" style="left:26px;top:47px;width:80px;height:100px"><div class="ph" role="img" aria-label="Woman in a yoga pose" style="height:52px;background:linear-gradient(#c9d6de,#8aa0ad)"></div><h5>OWNING YOUR STORY</h5><p>Empower yourself by embracing your unique journey as a catalyst for personal growth and success.</p></div>
    <div class="card" style="left:115px;top:47px;width:80px;height:100px"><div class="ph" role="img" aria-label="Woman at a laptop" style="height:52px;background:linear-gradient(#d6dde4,#8e9aa6)"></div><h5>UNLEASHING YOUR INNER POWER</h5><p>Harness self-confidence and belief to conquer obstacles and turn dreams into reality.</p></div>
    <div class="card" style="left:204px;top:47px;width:80px;height:100px"><div class="ph" role="img" aria-label="Woman working by a window" style="height:52px;background:linear-gradient(#e2e2e2,#9a9a9a)"></div><h5>RISING LEADERS</h5><p>Develop confidence, resilience, and vision in students to lead and succeed.</p></div>
    <div class="card" style="left:70px;top:163px;width:80px;height:100px"><div class="ph" role="img" aria-label="Woman stretching on a mat" style="height:52px;background:linear-gradient(#c9d6de,#8aa0ad)"></div><h5>ACTIVATING YOUR POTENTIAL</h5><p>Step into your calling with passion and clarity to shape purpose-driven life.</p></div>
    <div class="card" style="left:159px;top:163px;width:80px;height:100px"><div class="ph" role="img" aria-label="Woman writing at a desk" style="height:52px;background:linear-gradient(#e2e2e2,#9a9a9a)"></div><h5>REPLENISHING YOUR RESILIENCE</h5><p>Explore techniques to fortify resilience, back stronger from life's challenges.</p></div>
  </section>
  <section style="height:70px" class="center">
    <p class="h2" style="font-size:6px;padding-top:20px">BOOK CORINNE FOR YOUR EVENT</p>
    <span class="btn" style="margin-top:6px">Inquire About Speaking</span>
  </section>
  <div class="foot" style="height:65px"><div class="logo"><i></i><span>Corinne Albadeau</span></div><div class="sep"></div><div><div class="con">Connect With Corinne</div><div class="soc"><i></i><i></i><i></i><i></i></div></div><div class="cols"><div>Home<br>Videos<br>Virtual<br>Meeting Professionals</div><div>Workshops<br>About Corinne<br>Speaking</div></div></div>
  <div class="bottom">©Corinne Albadeau. All Rights Reserved.<br>Sitemap | Privacy Policy<span>EN</span></div>
</div>

<!-- PAGE 4 : COACH -->
<div class="page" style="left:1104px;height:1060px">
  <div class="topbar"><span>555-014-2270</span><span>Check Out Corinne's Latest Book: <b>SWEETHEART, RISE UP</b></span><span>hello@corinnealbadeau.com</span></div>
  <section class="hero" style="height:145px;background:linear-gradient(110deg,#2a2a2c,#4a4a4c 60%,#2c2c2e)">
    <div class="ph" role="img" aria-label="Corinne in a patterned top by a brick wall" style="right:25px;top:22px;width:100px;height:123px;background:linear-gradient(180deg,#5a5558,#262426)"></div>
    <div class="nav"><div class="logo"><i></i><span>Corinne Albadeau</span></div><ul><li>Home</li><li>About</li><li>Speaker</li><li class="on">Coach</li><li>Courses</li><li>Events</li><li>Shop</li><li class="btn">Contact Us</li></ul></div>
    <div class="abs" style="left:26px;top:56px;width:140px"><h1 style="font-size:8px;line-height:11px">COACHING</h1><p class="serif" style="font-size:4.3px;line-height:6px;color:#fff;margin-top:3px">TRANSFORM YOUR LIFE WITH<br>PERSONALIZED COACHING</p>
      <p style="margin-top:4px;font-size:2.5px;line-height:3.9px">Corinne Albadeau offers one-on-one coaching sessions designed to help women achieve their personal and professional goals. Her coaching approach is personalized, supportive, and results-driven, ensuring that each client receives the guidance and strategies they need to succeed.</p></div>
  </section>
  <section style="height:277px">
    <p class="h2" style="font-size:6px;padding-top:20px">COACHING SPECIALTIES</p>
    <div class="card" style="left:26px;top:38px;width:125px;height:105px"><div class="ph" role="img" aria-label="City skyline at sunset" style="height:52px;background:linear-gradient(#e0a070,#3a3040)"></div><h4>CONFIDENCE BUILDING</h4><p>Empowering individuals to recognize their strengths, overcome self-doubt, and cultivate confidence in themselves and their abilities.</p></div>
    <div class="card" style="left:159px;top:38px;width:125px;height:105px"><div class="ph" role="img" aria-label="Woman smiling at a laptop" style="height:52px;background:linear-gradient(#c8d0dc,#4a5a80)"></div><h4>LEADERSHIP AND EXECUTIVE COACHING</h4><p>Equipping aspiring and established leaders with the skills, mindset, and strategies needed to excel in their roles, inspire others, and drive organizational success.</p></div>
    <div class="card" style="left:26px;top:149px;width:125px;height:105px"><div class="ph" role="img" aria-label="Audience in a conference room" style="height:52px;background:linear-gradient(#c4b8a8,#6a5e52)"></div><h4>PERSONAL DEVELOPMENT</h4><p>Guiding clients on a journey of self-discovery, growth, and fulfillment, helping them unleash their potential and live authentically.</p></div>
    <div class="card" style="left:159px;top:149px;width:125px;height:105px"><div class="ph" role="img" aria-label="Colleagues shaking hands" style="height:52px;background:linear-gradient(#e2d8cc,#8a7a6c)"></div><h4>OVERCOMING PERSONAL OBSTACLES</h4><p>Supporting individuals in overcoming challenges, setbacks, and obstacles, empowering them to navigate life's difficulties with resilience and determination.</p></div>
  </section>
  <section style="height:143px;background:linear-gradient(90deg,#19181d,#26242a)">
    <div class="ph" role="img" aria-label="Corinne in a patterned blouse, arms crossed" style="left:30px;top:6px;width:100px;height:137px;background:linear-gradient(180deg,#4a3a38,#1a1718)"></div>
    <div class="abs" style="left:162px;top:26px;width:128px;color:#ddd">
      <p class="serif" style="font-size:5px;line-height:7px;color:#fff">WHY CHOOSE CORINNE AS<br>YOUR COACH?</p>
      <p style="font-size:2.5px;line-height:3.8px;margin-top:4px"><b style="color:#fff">Personalized Approach:</b> Tailors each session to address your unique goals and challenges.</p>
      <p style="font-size:2.5px;line-height:3.8px;margin-top:5px"><b style="color:#fff">Expert Guidance:</b> Leverages years of experience to provide practical and effective strategies.</p>
      <p style="font-size:2.5px;line-height:3.8px;margin-top:5px"><b style="color:#fff">Empowering Support:</b> Encourages and motivates you to reach your full potential.</p></div>
  </section>
  <section style="height:125px" class="center">
    <p class="h2" style="font-size:6px;padding-top:20px">CLIENT LOVE</p>
    <div class="ph" role="img" aria-label="Client portrait" style="left:144px;top:38px;width:22px;height:22px;border-radius:50%;background:linear-gradient(#e0b89a,#8a5a48)"></div>
    <p style="font-size:2.7px;line-height:4.3px;margin:46px 60px 0">"Corinne's coaching has been a game-changer for me. Her insights and guidance have helped me achieve goals I never thought possible."</p>
    <p class="serif" style="font-size:3.2px;color:#333;margin-top:4px">- OTTILIE</p>
  </section>
  <section style="height:68px;background:var(--mist)" class="center">
    <p class="h2" style="font-size:5.5px;padding-top:20px">START YOUR JOURNEY TO SUCCESS</p>
    <span class="btn" style="margin-top:6px">Book a Session</span>
  </section>
  <section style="height:177px">
    <p class="h2" style="font-size:6px;padding-top:22px">COACHING PACKAGES</p>
    <div class="abs center" style="left:25px;top:51px;width:80px;height:95px;border-bottom:.5px solid #ddd">
      <div style="background:var(--plum);color:#fff;font-size:2.8px;font-weight:600;height:18px;padding-top:7px">Quick Boost - 1 session</div>
      <div style="width:20px;height:20px;border-radius:50%;background:var(--plum);border:1.5px solid #fff;box-shadow:0 0 0 .5px var(--plum);color:#fff;font-size:4.5px;font-weight:700;line-height:17px;margin:-3px auto 0">$199</div>
      <p style="font-size:2.3px;line-height:3.6px;margin:8px 4px 0">Receive immediate, focused support and guidance tailored to your needs to kickstart your journey to success in a 45-minute session.</p></div>
    <div class="abs center" style="left:105px;top:44px;width:98px;height:116px;box-shadow:0 0 3px rgba(0,0,0,.15);background:#fff">
      <div style="background:var(--cyan);color:#fff;font-size:2.8px;font-weight:600;height:25px;padding-top:6px">Focused Growth 3 sessions</div>
      <div style="width:20px;height:20px;border-radius:50%;background:var(--cyan);border:1.5px solid #fff;box-shadow:0 0 0 .5px var(--cyan);color:#fff;font-size:4.5px;font-weight:700;line-height:17px;margin:-10px auto 0">$497</div>
      <p style="font-size:2.3px;line-height:3.6px;margin:10px 6px 0">Delve deeper into your goals and challenges with three personalized 45-minute coaching sessions, aimed at tangible progress and development.</p></div>
    <div class="abs center" style="left:203px;top:51px;width:80px;height:95px;border-bottom:.5px solid #ddd">
      <div style="background:var(--plum);color:#fff;font-size:2.8px;font-weight:600;height:18px;padding-top:7px">Growth Intensive 5 sessions</div>
      <div style="width:20px;height:20px;border-radius:50%;background:var(--plum);border:1.5px solid #fff;box-shadow:0 0 0 .5px var(--plum);color:#fff;font-size:4.5px;font-weight:700;line-height:17px;margin:-3px auto 0">$899</div>
      <p style="font-size:2.3px;line-height:3.6px;margin:8px 4px 0">Embark on an intensive transformative coaching journey over five 45-minute sessions, empowering significant personal and professional growth.</p></div>
  </section>
  <div class="foot" style="height:75px"><div class="logo"><i></i><span>Corinne Albadeau</span></div><div class="sep"></div><div><div class="con">Connect With Corinne</div><div class="soc"><i></i><i></i><i></i><i></i></div></div><div class="cols"><div>Home<br>Videos<br>Virtual<br>Meeting Professionals</div><div>Workshops<br>About Corinne<br>Speaking</div></div></div>
  <div class="bottom">©Corinne Albadeau. All Rights Reserved.<br>Sitemap | Privacy Policy<span>EN</span></div>
</div>

<!-- PAGE 5 : CONTACT -->
<div class="page" style="left:1455px;height:416px">
  <div class="topbar"><span>555-014-2270</span><span>Check Out Corinne's Latest Book: <b>SWEETHEART, RISE UP</b></span><span>hello@corinnealbadeau.com</span></div>
  <section class="hero" style="height:127px;background:linear-gradient(110deg,#2c2c2e,#4a4a4d 60%,#2e2e30)">
    <div class="ph" role="img" aria-label="Corinne in a red dress pointing forward" style="right:45px;top:22px;width:80px;height:105px;background:linear-gradient(180deg,#a03038,#4a1a1e)"></div>
    <div class="nav"><div class="logo"><i></i><span>Corinne Albadeau</span></div><ul><li>Home</li><li>About</li><li>Speaker</li><li>Coach</li><li>Courses</li><li>Events</li><li>Shop</li><li class="btn">Contact Us</li></ul></div>
    <h1 class="abs" style="left:26px;top:60px;font-size:8px">CONTACT US</h1>
  </section>
  <section style="height:178px">
    <p class="h2" style="font-size:6px;padding-top:22px">GET IN TOUCH</p>
    <div class="abs" style="left:26px;top:44px;width:100px">
      <div style="display:flex;gap:6px;margin-bottom:8px"><svg width="18" height="18" viewBox="0 0 18 18"><circle cx="9" cy="9" r="9" fill="var(--plum)"/><path d="M9 4.5a3 3 0 0 1 3 3c0 2.2-3 5.5-3 5.5s-3-3.3-3-5.5a3 3 0 0 1 3-3z" fill="none" stroke="#fff" stroke-width=".8"/><circle cx="9" cy="7.5" r="1" fill="#fff"/></svg><p style="font-size:2.3px;line-height:3.5px;color:#333"><b>ADDRESS:</b><br>120 Lantern Row, Suite 4<br>Maplewood, GA 30000</p></div>
      <div style="display:flex;gap:6px;margin-bottom:8px"><svg width="18" height="18" viewBox="0 0 18 18"><circle cx="9" cy="9" r="9" fill="var(--plum)"/><path d="M6.5 5c.6-.4 1 0 1.3.6l.5 1c.2.5 0 .8-.4 1.1.4 1 1.2 1.8 2.2 2.2.3-.4.6-.6 1.1-.4l1 .5c.6.3 1 .7.6 1.3-.6.9-1.6 1.2-2.6.8A7 7 0 0 1 5.8 7.6c-.4-1 0-2 .7-2.6z" fill="#fff"/></svg><p style="font-size:2.3px;line-height:3.5px;color:#333"><b>PHONE:</b><br>555-014-2270</p></div>
      <div style="display:flex;gap:6px"><svg width="18" height="18" viewBox="0 0 18 18"><circle cx="9" cy="9" r="9" fill="var(--plum)"/><rect x="5" y="6" width="8" height="6" fill="#fff"/><path d="M5 6l4 3.2L13 6" fill="none" stroke="var(--plum)" stroke-width=".7"/></svg><p style="font-size:2.3px;line-height:3.5px;color:#333"><b>EMAIL:</b><br>hello@corinnealbadeau.com</p></div>
    </div>
    <div class="abs" style="left:130px;top:44px;width:150px;display:grid;grid-template-columns:1fr 1fr;gap:3px">
      <div class="field" style="height:8px;background:#f7f7f9;border-color:#eee">First Name</div><div class="field" style="height:8px;background:#f7f7f9;border-color:#eee">Last Name</div>
      <div class="field" style="height:8px;background:#f7f7f9;border-color:#eee">Phone Number</div><div class="field" style="height:8px;background:#f7f7f9;border-color:#eee">Email</div>
      <div class="field" style="grid-column:span 2;height:30px;background:#f7f7f9;border-color:#eee">Message</div>
    </div>
    <span class="btn abs" style="left:130px;top:110px;font-family:Montserrat,sans-serif;font-size:2.4px;font-weight:700">SEND MESSAGE</span>
    <p class="serif abs" style="left:130px;top:136px;font-size:3.8px;color:#333">SOCIAL MEDIA</p>
    <div class="abs" style="left:138px;top:147px;display:flex;gap:3px"><i style="width:5px;height:5px;border:.5px solid var(--plum);border-radius:50%"></i><i style="width:5px;height:5px;border:.5px solid var(--plum);border-radius:50%"></i><i style="width:5px;height:5px;border:.5px solid var(--plum);border-radius:50%"></i></div>
  </section>
  <div class="foot" style="height:60px"><div class="logo"><i></i><span>Corinne Albadeau</span></div><div class="sep"></div><div><div class="con">Connect With Corinne</div><div class="soc"><i></i><i></i><i></i><i></i></div></div><div class="cols"><div>Home<br>Videos<br>Virtual<br>Meeting Professionals</div><div>Workshops<br>About Corinne<br>Speaking</div></div></div>
  <div class="bottom">©Corinne Albadeau. All Rights Reserved.<br>Sitemap | Privacy Policy<span>EN</span></div>
</div>

</div>
</body>
</html>
```